New Business card design to reflect rebrand

I would like a business card design with a good base colour for our new logo and also a placeholder for a profile pic of the card holder. the design needs to be editable to the point that we can easily change the picture of the person and use that design for printmoor etc. we are looking at a metalic finish business card so will need a good base colour to bring out the finish.

Target Market(s)

prospective customers

Industry/Entity Type

Business

Contact Information for Business Card

I would like one editable design that we can change the name of the card holder and profile picture. The design need to be in a format that be send to printmoor etc.

Our address is Fenwick Lodge, Mill Lane, Ashcombe Green, RG41 3TQ Tel no. 01632 960417

Requirements
Must have
• place holder for a profile pic for the card holder. in AI or preferably PSD format

```html
<!DOCTYPE html>
<html lang="en">
<head>
<meta charset="utf-8">
<title>Halvern Workplace Services – Business Card</title>
<link rel="stylesheet" href="https://fonts.googleapis.com/css2?family=Arimo:wght@400;700&display=swap">
<style>
  :root {
    --stage: #e9e6e1;
    --metal-light: #eeeff0;
    --metal-mid: #cfd1d3;
    --metal-dark: #b7babd;
    --navy: #3f5674;
    --orange: #f26a21;
    --white: #ffffff;
    --grey-text: #55595e;
    --photo-warm: #8b6a55;
    --photo-deep: #3b2d26;
  }
  * { box-sizing: border-box; margin: 0; padding: 0; }
  html, body { width: 1200px; height: 784px; overflow: hidden; }
  body {
    background: var(--stage);
    font-family: "Arimo", Arial, sans-serif;
    position: relative;
  }
  .card {
    position: absolute;
    top: 232px;
    width: 560px;
    height: 320px;
    border-radius: 6px;
    overflow: hidden;
    background:
      repeating-linear-gradient(0deg, rgba(255,255,255,.35) 0 1px, rgba(0,0,0,.05) 1px 2px, transparent 2px 3px),
      linear-gradient(160deg, var(--metal-light), var(--metal-mid) 55%, var(--metal-dark));
    box-shadow: 0 6px 18px rgba(0,0,0,.18);
  }
  .card-back { left: 20px; }
  .card-front { left: 620px; }

  .back-name {
    position: absolute; inset: 0;
    display: flex; align-items: center; justify-content: center;
    font-size: 64px; font-weight: 700; letter-spacing: 4px;
    color: #9a9ea2;
  }

  .holder { position: absolute; top: 18px; right: 22px; text-align: right; }
  .holder-name { color: var(--orange); font-size: 15px; }
  .holder-role { color: var(--grey-text); font-size: 10px; margin-top: 2px; }

  .brand {
    position: absolute; left: 34px; top: 78px;
    display: flex; align-items: center; gap: 10px;
  }
  .brand-mark { width: 26px; height: 26px; background: var(--navy); }
  .brand-name {
    color: var(--navy); font-size: 30px; font-weight: 700; line-height: 1.05;
    width: 330px;
  }

  .contact-band {
    position: absolute; left: 0; right: 0; top: 196px; height: 104px;
    background: var(--navy);
    border-top: 3px solid var(--orange);
    border-bottom: 3px solid var(--orange);
  }
  .band-trim {
    position: absolute; left: 0; right: 0; top: 304px; height: 4px;
    background: var(--orange);
  }
  .contact-list {
    list-style: none;
    position: absolute; left: 60px; top: 8px;
  }
  .contact-list li {
    display: flex; align-items: center; gap: 7px;
    color: var(--white); font-size: 14px; line-height: 17.5px;
  }
  .contact-list svg { width: 13px; height: 13px; flex: none; }

  .profile-photo {
    position: absolute; right: 20px; top: 62px;
    width: 160px; height: 246px;
    background: linear-gradient(180deg, var(--photo-warm), var(--photo-deep));
  }
</style>
</head>
<body>

<section class="card card-back">
  <div class="back-name">HALVERN</div>
</section>

<section class="card card-front">
  <div class="holder">
    <p class="holder-name">Dana Morrell VP</p>
    <p class="holder-role">Manager</p>
  </div>

  <div class="brand">
    <span class="brand-mark"></span>
    <p class="brand-name">Halvern Workplace Services</p>
  </div>

  <div class="contact-band">
    <ul class="contact-list">
      <li>
        <svg viewBox="0 0 14 14"><rect x="3" y="1" width="8" height="4" fill="none" stroke="#f26a21" stroke-width="1.4"/><rect x="1" y="5" width="12" height="5" fill="#f26a21"/><rect x="3" y="9" width="8" height="4" fill="none" stroke="#f26a21" stroke-width="1.4"/></svg>
        214-555-0143
      </li>
      <li>
        <svg viewBox="0 0 14 14"><path d="M3 1l3 3-1.5 1.5a7 7 0 0 0 4 4L10 8l3 3-2 2C5 13 1 9 1 3z" fill="#f26a21"/></svg>
        214-555-0178
      </li>
      <li>
        <svg viewBox="0 0 14 14"><rect x="1" y="3" width="12" height="8" fill="#f26a21"/><path d="M1 3l6 5 6-5" fill="none" stroke="#3f5674" stroke-width="1.2"/></svg>
        dana@halvernworks.com
      </li>
      <li>
        <svg viewBox="0 0 14 14"><circle cx="7" cy="7" r="5.8" fill="none" stroke="#f26a21" stroke-width="1.3"/><ellipse cx="7" cy="7" rx="2.4" ry="5.8" fill="none" stroke="#f26a21" stroke-width="1.1"/><path d="M1.2 7h11.6" stroke="#f26a21" stroke-width="1.1"/></svg>
        www.halvernworks.com
      </li>
      <li>
        <svg viewBox="0 0 14 14"><path d="M7 1l6 6h-2v6H8V9H6v4H3V7H1z" fill="#f26a21"/></svg>
        418 Kestrel Ave. Larkfield, TX 75390
      </li>
    </ul>
  </div>
  <div class="band-trim"></div>

  <div class="profile-photo" role="img" aria-label="Profile photo of the card holder"></div>
</section>

</body>
</html>
```